Re-design of 4 x 2-sided reports

I need the 4 attached reports (3 are 2-sides of A4; 1 is 7-sides of A4) to be re-designed with a consistent look and feel. Just need 1 or 2 images per report being inserted plus consistent branding and contact details being displayed in the same location on each report with same colour, font and design). Reports are attached.
The reports are used as lead magnets.
That is, visitors to our website can download one of them (7 Steps To Sharpen Your Sales Over The Coming Month) by filling in a form with their email address. Then over the next 30 days the other reports are sent to the subscriber via email autoresponders.
Blue Harbour Marketing is a marketing consultancy dealing with companies in the North West of England providing cost-effective and profitable marketing to small and medium-sized businesses that want better and quicker results. The reports need to be professional and corporate looking. Please let me know if you need any further clarification or have any questions. I attach an example report. I don't necessarily want to mirror this report (from the law firm) but it may help to understand what look I'm trying to get. Many thanks, Gordon

Target Market(s)

SMEs based in NW of England
Typically with turnover of £1m to £10m or 10 to 100 employees
Clients often in the construction sector, healthcare, accountants, lawyers and local councils.

Industry/Entity Type

Marketing

Font styles to use
Serif
Sans Serif

Colors
ec1f27

Requirements
Must have
• Consistent branding
• Logo in same place across all four reports
• Contact details in same place across all four reports
• Same font across all four reports
• Same colour across all four reports
• Professional and bold look
Nice to have
• Some strong stock photography
• 1 or 2 images per report
• More images for the 7-page report though
Should not have
• No graphics

```html
<!DOCTYPE html>
<html lang="en">
<head>
<meta charset="utf-8">
<title>17 Reasons Why Your Website Is Not Getting Found On The Internet – Blue Harbour Marketing</title>
<link rel="stylesheet" href="https://fonts.googleapis.com/css2?family=Roboto:wght@300;700&family=Open+Sans:ital,wght@0,400;0,700;1,400&display=swap">
<style>
  :root {
    --brand-red: #c4161c;
    --brand-red-deep: #b3151b;
    --ink: #1d1d1d;
    --muted: #444444;
    --paper: #ffffff;
    --backdrop: #e3e3e3;
    --sky-top: #5d83a8;
    --sky-mid: #b9c9d8;
    --city: #7c8590;
  }
  * { box-sizing: border-box; margin: 0; padding: 0; }
  html, body { width: 1200px; height: 848px; overflow: hidden; }
  body {
    background: var(--backdrop);
    font-family: "Open Sans", Arial, sans-serif;
    color: var(--ink);
    position: relative;
  }
  .page {
    position: absolute;
    background: var(--paper);
    box-shadow: 4px 5px 8px rgba(0,0,0,0.28);
    overflow: hidden;
  }

  /* Cover */
  .cover { left: 40px; top: 22px; width: 554px; height: 784px; }
  .brand-mark {
    position: absolute; left: 53px; top: 74px; width: 104px;
    display: flex; flex-direction: column; align-items: center;
  }
  .brand-mark .square { width: 98px; height: 96px; background: var(--brand-red); }
  .brand-mark .name {
    margin-top: 8px; font-family: "Roboto", Arial, sans-serif; font-weight: 700;
    font-size: 14px; line-height: 1.15; text-align: center; color: var(--brand-red);
  }
  .cover-title {
    position: absolute; left: 189px; top: 66px;
    font-family: "Roboto", Arial, sans-serif; font-size: 35px; line-height: 40px;
    color: var(--brand-red);
  }
  .cover-title .lead { display: block; font-weight: 300; color: var(--ink); }
  .cover-title .bold { display: block; font-weight: 700; }
  .cover-title .light { display: block; font-weight: 300; }
  .cover-photo {
    position: absolute; left: 0; top: 261px; width: 554px; height: 381px;
    background: linear-gradient(180deg, var(--sky-top) 0%, var(--sky-mid) 55%, #d7dde3 72%, var(--city) 100%);
  }
  .cover-url {
    position: absolute; left: 0; right: 0; top: 674px; text-align: center;
    font-weight: 700; font-size: 14px; letter-spacing: 0.3px; color: var(--brand-red);
  }
  .cover-rule {
    position: absolute; left: 203px; top: 708px; width: 146px; height: 1px; background: var(--muted);
  }
  .cover-tagline {
    position: absolute; left: 0; right: 0; top: 723px; text-align: center;
    font-style: italic; font-size: 13px; color: var(--muted);
  }
  .cover-copyright {
    position: absolute; left: 0; right: 0; top: 747px; text-align: center;
    font-size: 7px; color: var(--muted);
  }

  /* Reasons page */
  .reasons { left: 609px; top: 25px; width: 552px; height: 781px; }
  .reason-list {
    list-style: none; position: absolute; left: 51px; top: 60px; width: 456px;
    font-size: 12.6px; line-height: 16.5px;
  }
  .reason-list li { margin-bottom: 10px; }
  .reason-list .num {
    display: inline-block; width: 34px; color: var(--brand-red); font-size: 11px;
  }
  .contact-band {
    position: absolute; left: 0; right: 0; bottom: 0; height: 50px;
    background: var(--brand-red-deep); color: #fff;
    display: flex; align-items: center;
  }
  .contact-band .band-brand {
    width: 120px; padding-left: 50px; font-family: "Roboto", Arial, sans-serif;
    font-weight: 700; font-size: 10px; line-height: 1.1;
  }
  .contact-band .details { font-size: 10.5px; margin-left: 14px; }
</style>
</head>
<body>

<section class="page cover">
  <div class="brand-mark">
    <div class="square"></div>
    <div class="name">Blue Harbour Marketing</div>
  </div>
  <h1 class="cover-title">
    <span class="lead">17 Reasons</span>
    <span class="bold">Why Your Website</span>
    <span class="light">Is Not Getting Found</span>
    <span class="bold">On The Internet</span>
  </h1>
  <div class="cover-photo" role="img" aria-label="Photo of a businessman on a stepladder looking through binoculars over a city skyline under a cloudy blue sky"></div>
  <p class="cover-url">www.BlueHarbourMarketing.co.uk</p>
  <div class="cover-rule"></div>
  <p class="cover-tagline">Your “Blue Harbour Marketing” FREE Report</p>
  <p class="cover-copyright">© Copyright 2016 Blue Harbour Marketing. All Rights Reserved</p>
</section>

<section class="page reasons">
  <ol class="reason-list">
    <li><span class="num">1.</span>Your site has not been ‘optimised’ for Searchly, Quester &amp; Lookabout - the 3 main search engines in the UK</li>
    <li><span class="num">2.</span>You have no regular, fresh content</li>
    <li><span class="num">3.</span>The content you do post is not valuable to your potential customers</li>
    <li><span class="num">4.</span>Your website has some spelling mistakes and grammatical errors so the search engines are penalising you</li>
    <li><span class="num">5.</span>You’ve let someone previously add lots of keywords on each page - known as ‘keyword stuffing’ - and Searchly has penalised you</li>
    <li><span class="num">6.</span>You haven’t described each page from the point of view of what the visitor can expect to read</li>
    <li><span class="num">7.</span>How people navigate from page to page to find what they are looking for is not clear or intuitive</li>
    <li><span class="num">8.</span>You may not be using social media to drive traffic to your website</li>
    <li><span class="num">9.</span>You may not be doing the right kind of marketing to get people to visit your website (Are you doing any marketing?)</li>
    <li><span class="num">10.</span>You haven’t taken advantage of the Searchly Local Listings facility to make people aware of your business in your local area</li>
    <li><span class="num">11.</span>You haven’t created an XML Sitemap and submitted it to the search engines so your website can be ‘reviewed’ by them</li>
    <li><span class="num">12.</span>You haven’t properly described each image on your website</li>
    <li><span class="num">13.</span>You may not have analysed your competitors’ website - content, structure and metadata - and configured your website accordingly</li>
    <li><span class="num">14.</span>You may not be using the right keywords on your website to describe your business, its products or services</li>
    <li><span class="num">15.</span>You may not have submitted your website to certain directories or social bookmarking sites</li>
    <li><span class="num">16.</span>You may not have used simple to understand names for your pages of your website e.g. yourcompanyname.co.uk/ourproductname</li>
    <li><span class="num">17.</span>You may have your website hosted overseas or with be using a .com address</li>
  </ol>
  <footer class="contact-band">
    <div class="band-brand">Blue Harbour Marketing</div>
    <p class="details">www.BlueHarbourMarketing.co.uk &nbsp;|&nbsp; 01632 960 418 &nbsp;|&nbsp; info@blueharbourmarketing.co.uk</p>
  </footer>
</section>

</body>
</html>
```